Brook Forge - Crypto Currency Miner Powered by Renewable Energy Website

We Need Web Pages Design for Website for Crypto Currency Miner

Serivices include:
Mining Rig Sales
Housing for Rigs turnkey on renewable energy grid
Cloud Mining term packages
Updates

http://www.vaultrigratings.example (Competitors sites)

Target Market(s)

Investers for Mining Rigs and terms for 1,2 or 3 years of Hash rate

Industry/Entity Type

Mining

Number of Pages Required

5+ page

Font styles to use
Sans Serif

Colors
add136
9bcb3c
606060
474747
ffc214
cadf82
fbee3e
876aae
6b449b

Requirements
Must have
• Pictures of Solar, Wind and power Factor Correction units
Nice to have
• e-commerce platform so contract terms can be purchased through website
Should not have
• Heavy construction equipment

```html
<!DOCTYPE html>
<html lang="en">
<head>
<meta charset="utf-8">
<title>Brook Forge – Renewable Crypto Mining</title>
<link rel="stylesheet" href="https://fonts.googleapis.com/css2?family=Open+Sans:wght@400;600;700&family=Oswald:wght@500&display=swap">
<style>
:root{
  --green:#22a03c;
  --green-dark:#1b8a32;
  --green-light:#9bcb3c;
  --text:#474747;
  --muted:#606060;
  --grey-bg:#ebe9e6;
  --team-bg:#f4f3f1;
  --dark:#1c1c1c;
  --footer:#252525;
  --white:#ffffff;
}
*{box-sizing:border-box;margin:0;padding:0}
html,body{width:1200px;height:4523px;overflow:hidden}
body{font-family:"Open Sans",Arial,sans-serif;color:var(--text);background:var(--white);font-size:13px;line-height:1.6}
a{color:inherit;text-decoration:none}
.brand{display:flex;align-items:center;gap:10px;font-weight:700;color:var(--green);font-size:22px}
.brand-dot{width:34px;height:34px;border-radius:50%;background:var(--green)}
.section-title{display:flex;align-items:center;justify-content:center;gap:12px;font-size:36px;font-weight:400;color:var(--text)}
.title-dot{width:40px;height:40px;border-radius:50%;background:var(--green)}
.btn{display:inline-block;border-radius:20px;font-size:11px;font-weight:600;text-transform:uppercase;padding:9px 40px;letter-spacing:.5px}
.btn-green{background:var(--green);color:var(--white)}
.btn-ghost{border:2px solid var(--white);color:var(--white)}
.btn-white{background:var(--white);color:var(--green)}

/* header */
.topbar{height:142px;display:flex;align-items:center;justify-content:space-between;padding:0 180px}
.topbar .phone{display:flex;align-items:center;gap:8px;font-weight:700;font-size:20px;color:#111}
.topbar .phone svg{width:22px;height:22px}
.topbar .brand{flex-direction:column;gap:4px;font-size:20px}
.social{display:flex;gap:6px}
.social span{width:22px;height:22px;border-radius:50%;background:var(--green)}
.mainnav{height:51px;background:var(--green);display:flex;justify-content:center;align-items:center;gap:36px;color:var(--white);font-size:13px;font-weight:600}
.mainnav .sep{opacity:.7}
.mainnav .active{text-decoration:underline;text-underline-offset:6px}

/* hero */
.hero{height:507px;position:relative;background:linear-gradient(180deg,#2b2f33,#15181b 60%,#30353a);text-align:center;color:var(--white)}
.hero h1{position:absolute;top:150px;width:100%;font-size:80px;font-weight:700;color:var(--green);line-height:1}
.hero p{position:absolute;top:240px;width:100%;font-size:30px;font-weight:700}
.hero .actions{position:absolute;top:298px;width:100%;display:flex;justify-content:center;gap:40px}
.hero .dots{position:absolute;bottom:28px;width:100%;display:flex;justify-content:center;gap:8px}
.hero .dots span{width:9px;height:9px;border-radius:50%;background:rgba(255,255,255,.5)}
.hero .dots span:first-child{background:var(--green)}

/* about */
.about{height:530px;position:relative}
.about .media{position:absolute;left:181px;top:102px;width:368px;height:301px;border:1px solid #d8d8d8;background:linear-gradient(160deg,#ffffff,#d7ecf6 60%,#b9dcee)}
.about .copy{position:absolute;left:603px;top:100px;width:415px}
.about h2{display:flex;align-items:center;gap:12px;font-size:36px;font-weight:400}
.about .lead{font-weight:700;font-size:14px;margin:10px 0 18px}
.about .body{font-size:12px;color:var(--muted)}
.about .btn{margin-top:26px}

/* services */
.services{height:895px;background:var(--grey-bg);padding-top:72px;text-align:center}
.services .intro{width:780px;margin:30px auto 0;font-size:12px;color:var(--muted)}
.service-cards{display:flex;justify-content:center;gap:24px;margin-top:58px}
.service-card{width:264px;height:537px;background:var(--green);border:4px solid var(--green-light);position:relative;color:var(--white)}
.service-card .photo{height:170px}
.service-card .icon{position:absolute;top:124px;left:50%;margin-left:-55px;width:110px;height:110px;border-radius:50%;background:var(--white);border:6px solid var(--green-dark);display:flex;align-items:center;justify-content:center}
.service-card .icon span{width:58px;height:58px;border-radius:50%;background:var(--green)}
.service-card h3{margin-top:86px;font-size:15px;font-weight:700;padding:0 20px;line-height:1.3}
.service-card p{font-size:11px;padding:14px 24px 0;line-height:1.55}
.service-card .btn{position:absolute;bottom:28px;left:50%;transform:translateX(-50%);padding:7px 34px;font-size:10px}

/* cloud mining */
.cloud{height:733px;position:relative;text-align:center;padding-top:56px}
.cloud .intro{width:700px;margin:28px auto 0;font-size:12px;color:var(--muted)}
.plans{position:absolute;top:212px;left:241px;display:flex;gap:18px}
.plan{width:224px;height:422px;border-radius:18px;background:linear-gradient(180deg,#141414,#222);border:4px solid var(--green-light);color:var(--white);overflow:hidden}
.plan .head{height:56px;line-height:56px;font-size:11px;font-weight:700;color:var(--green-light);border-bottom:1px solid #3a3a3a;text-transform:uppercase}
.plan .algo{font-size:11px;font-weight:700;padding:12px 0 6px;text-transform:uppercase}
.plan .row{font-size:9.5px;padding:6px 0;color:#ddd}
.plan .price-box{margin-top:18px;background:var(--green);height:118px;padding-top:20px}
.plan .price{font-size:38px;font-weight:700;line-height:1}
.plan .per{font-size:9px;margin-top:6px}
.plan .buy{display:inline-block;margin-top:16px;background:#7a7a7a;font-size:9px;padding:5px 20px;text-transform:uppercase}
.plan .buy{margin-top:14px}
.arrow{position:absolute;width:24px;height:40px}

/* why us */
.why{height:277px;background:var(--green);color:var(--white);text-align:center;padding-top:44px}
.why h2{display:flex;justify-content:center;align-items:center;gap:12px;font-size:36px;font-weight:400}
.why h2 .title-dot{background:var(--white)}
.why p{width:1000px;margin:18px auto 0;font-size:15px;line-height:1.45}

/* team */
.team{height:453px;background:var(--team-bg);position:relative;padding-top:44px}
.members{position:absolute;top:97px;left:232px;display:flex;gap:22px}
.member{width:168px;height:271px;background:var(--white);text-align:center;padding-top:20px;box-shadow:0 1px 3px rgba(0,0,0,.08)}
.member .avatar{width:88px;height:88px;border-radius:50%;margin:0 auto;background:linear-gradient(160deg,#d9d4cf,#9d948c);border:3px solid #eee}
.member h4{color:var(--green);font-size:13px;font-weight:700;margin-top:12px;text-transform:uppercase}
.member .role{font-size:9px;color:#999;line-height:1.4;padding:4px 20px 10px;border-bottom:1px solid #eee;margin:0 14px}
.member .contact{font-size:9px;color:#777;text-align:left;padding:10px 16px 0;display:flex;flex-direction:column;gap:12px}
.member .contact span{display:flex;align-items:center;gap:8px}
.member .contact i{width:10px;height:10px;background:var(--green);display:inline-block;border-radius:2px}

/* signup */
.signup{height:120px;background:linear-gradient(90deg,#111,#2a2a2a 40%,#1a1a1a);display:flex;align-items:center;padding-left:100px;gap:14px}
.signup h3{font-family:"Oswald",Arial,sans-serif;font-weight:500;font-size:32px;color:var(--white);text-transform:uppercase;margin-right:16px;letter-spacing:.5px}
.field{width:186px;height:38px;background:#444;color:#ddd;font-size:12px;display:flex;align-items:center;padding-left:14px;gap:10px}
.field i{width:12px;height:12px;background:#ddd;border-radius:2px}
.signup .submit{width:100px;height:38px;background:var(--green);color:var(--white);font-size:12px;display:flex;align-items:center;justify-content:center}

/* testimonials */
.testimonials{height:407px;padding-top:48px}
.quotes{display:grid;grid-template-columns:460px 460px;column-gap:80px;row-gap:40px;margin:54px 0 0 190px}
.quote{display:flex;gap:18px}
.quote .avatar{width:64px;height:64px;border-radius:50%;flex:none;background:linear-gradient(160deg,#e3ddd6,#a79b90)}
.quote p{font-size:11px;color:#999;line-height:1.45}
.quote .who{font-size:11px;color:var(--text);margin-top:4px}
.quote .who b{color:var(--green)}

/* footer */
.footer{height:356px;background:var(--footer);color:#ccc;display:flex;padding:76px 0 0 190px;gap:0}
.footer .col-brand{width:240px;font-size:12px;line-height:1.4}
.footer .col-brand .brand{flex-direction:column;align-items:flex-start;color:var(--white);font-size:18px;margin-bottom:14px}
.footer .col-brand p{color:var(--white);margin-bottom:12px}
.footer .lines{display:flex;flex-direction:column;gap:4px;font-size:11px}
.footer .lines span{display:flex;align-items:center;gap:8px}
.footer .lines i{width:10px;height:10px;background:var(--green);border-radius:2px}
.footer .col-links{width:300px;border-left:1px solid #444;padding-left:80px;height:220px}
.footer h5{color:var(--green);font-size:16px;font-weight:400;text-transform:uppercase;letter-spacing:1px;padding-bottom:6px;border-bottom:1px solid #555;width:140px;margin-bottom:14px}
.footer ul{list-style:none;font-size:13px;color:var(--white)}
.footer li{margin-bottom:2px}
.footer li::before{content:"→";color:var(--green);margin-right:8px}
.footer .col-follow{border-left:1px solid #444;padding-left:80px;height:220px}
.footer .col-follow .social span{background:var(--white);width:14px;height:14px;border-radius:2px;margin-right:10px}
.footer .call{margin-top:40px}
.footer .call strong{display:block;color:var(--white);font-size:24px;font-weight:700}
.bottombar{height:52px;background:var(--dark);color:#aaa;font-size:10px;display:flex;align-items:center;justify-content:center}
</style>
</head>
<body>

<header>
  <div class="topbar">
    <div class="phone">
      <svg viewBox="0 0 24 24"><circle cx="12" cy="12" r="12" fill="#111"/><path d="M8.5 6.5l2 2-1.3 1.6c.7 1.6 2 2.9 3.7 3.7l1.6-1.3 2 2-1.2 2c-4.2-.3-8.5-4.6-8.8-8.8z" fill="#fff"/></svg>
      1-888-555-0142
    </div>
    <div class="brand"><span class="brand-dot"></span>Brook Forge</div>
    <div class="social"><span></span><span></span><span></span><span></span></div>
  </div>
  <nav class="mainnav">
    <a class="active">Home</a><span class="sep">|</span>
    <a>About</a><span class="sep">|</span>
    <a>Services</a><span class="sep">|</span>
    <a>Cloud Mining</a><span class="sep">|</span>
    <a>Why Us</a><span class="sep">|</span>
    <a>Our Team</a><span class="sep">|</span>
    <a>Contact Us</a>
  </nav>
</header>

<section class="hero" role="img" aria-label="Rows of mining server racks in a data centre">
  <h1>Start Mining Today!</h1>
  <p>Your state-of-the-art mining hardware is already running!</p>
  <div class="actions"><a class="btn btn-green">Start Now</a><a class="btn btn-ghost">Buy Now</a></div>
  <div class="dots"><span></span><span></span><span></span><span></span><span></span></div>
</section>

<section class="about">
  <div class="media" role="img" aria-label="Illustration of a cloud connected to a network of nodes"></div>
  <div class="copy">
    <h2><span class="title-dot"></span>About</h2>
    <p class="lead">Lorem ipsum dolor sit amet, consectetur adipiscing elit, sed do eiusmod tempor incididunt ut labore et</p>
    <p class="body">Ut enim ad minim veniam, quis nostrud exercitation ullamco laboris nisi ut aliquip ex ea commodo consequat. Duis aute irure dolor in reprehenderit in voluptate velit esse cillum dolore eu fugiat nulla pariatur. Lorem ipsum dolor sit amet, consectetur adipiscing elit, sed do eiusmod tempor incididunt ut labore et dolore magna aliqua, sed quia consequuntur magni dolores eos qui ratione voluptatem.</p>
    <a class="btn btn-green">Read More</a>
  </div>
</section>

<section class="services">
  <h2 class="section-title"><span class="title-dot"></span>Services</h2>
  <p class="intro">Ut enim ad minim veniam, quis nostrud exercitation ullamco laboris nisi ut aliquip ex ea commodo consequat. Duis aute irure dolor in reprehenderit in voluptate velit esse cillum dolore eu fugiat nulla pariatur.</p>
  <div class="service-cards">
    <article class="service-card">
      <div class="photo" role="img" aria-label="Mining rig server aisle" style="background:linear-gradient(180deg,#3a4048,#1b1f24)"></div>
      <div class="icon"><span></span></div>
      <h3>Mining Rig Sales</h3>
      <p>Lorem ipsum dolor sit amet, consectetur adipiscing elit. Quid autem habent admirations, cum prope accessit? An hoc usque quaque, aliter in vita? Non ignor de improbo, sed de callido improbo quaerimus.</p>
      <a class="btn btn-white">Read More</a>
    </article>
    <article class="service-card">
      <div class="photo" role="img" aria-label="Glowing coin with fire and light effects" style="background:linear-gradient(135deg,#1c3f8a,#6a3a5a 50%,#e0722a)"></div>
      <div class="icon"><span></span></div>
      <h3>Housing for Rigs turnkey on renewable energy grid</h3>
      <p>Lorem ipsum dolor sit amet, consectetur adipiscing elit. Quid autem habent admirations, cum prope accessit? An hoc usque quaque, aliter in vita? Non ignor de improbo, sed de callido improbo.</p>
      <a class="btn btn-white">Read More</a>
    </article>
    <article class="service-card">
      <div class="photo" role="img" aria-label="Solar panels and wind turbines under blue sky" style="background:linear-gradient(180deg,#8fc2ea,#4f7fb0 55%,#2c4a72)"></div>
      <div class="icon"><span></span></div>
      <h3>Cloud Mining term packages</h3>
      <p>Create your first cloud mining contract here! The most advanced mining hardware and only freshly mined coins. Start hashing immediately! Escape the noise, costly electricity bills, and warranty headaches.</p>
      <a class="btn btn-white">Read More</a>
    </article>
  </div>
</section>

<section class="cloud">
  <h2 class="section-title"><span class="title-dot"></span>Cloud Mining</h2>
  <p class="intro">Create your first cloud mining contract here! The most advanced mining hardware and only freshly mined coins. Start hashing immediately! Escape the noise, costly electricity bills, and warranty headaches.</p>
  <svg class="arrow" style="left:178px;top:400px" viewBox="0 0 24 40"><path d="M18 6L6 20l12 14" stroke="#22a03c" stroke-width="5" fill="none"/></svg>
  <div class="plans">
    <article class="plan">
      <div class="head">Ethrion Cloud Mining</div>
      <div class="algo">Ethash Algorithm Miner</div>
      <div class="row">Minimum Hashrate: 100 KH/s</div>
      <div class="row">Maintenance fee: <b>NONE</b></div>
      <div class="row">Hardware: GPU Rigs</div>
      <div class="row">Automatic payout in ETR</div>
      <div class="row">In Stock</div>
      <div class="row">1 year contract</div>
      <div class="price-box"><div class="price">$2.20</div><div class="per">per 100 KH/s</div><span class="buy">Buy Now</span></div>
    </article>
    <article class="plan">
      <div class="head">Zephcoin Cloud Mining</div>
      <div class="algo">Equihash Algorithm Miner</div>
      <div class="row">Minimum Hashrate: 1 H/s</div>
      <div class="row">Maintenance fee: <b>NONE</b></div>
      <div class="row">Hardware: GPU Rigs</div>
      <div class="row">Automatic payout in ZPH</div>
      <div class="row">In Stock</div>
      <div class="row">1 year contract</div>
      <div class="price-box"><div class="price">$2.00</div><div class="per">per 1 H/s</div><span class="buy">Buy Now</span></div>
    </article>
    <article class="plan">
      <div class="head">Dashel Cloud Mining</div>
      <div class="algo">X11 Algorithm Miner</div>
      <div class="row">Minimum Hashrate: 1 MH/s</div>
      <div class="row">Maintenance fee: <b>NONE</b></div>
      <div class="row">Hardware: Multi Factor</div>
      <div class="row">Automatic payout in DSL</div>
      <div class="row">Out of stock</div>
      <div class="row">1 year contract</div>
      <div class="price-box"><div class="price">$3.20</div><div class="per">per 1 MH/s</div><span class="buy">Buy Now</span></div>
    </article>
  </div>
  <svg class="arrow" style="left:998px;top:400px" viewBox="0 0 24 40"><path d="M6 6l12 14L6 34" stroke="#22a03c" stroke-width="5" fill="none"/></svg>
</section>

<section class="why">
  <h2><span class="title-dot"></span>Why Us</h2>
  <p>Lorem ipsum dolor sit amet, consectetur adipiscing elit. Quid autem habent admirations, cum prope accessis? An hoc usque quaque, aliter in vita? Non igitur de improbo, sed de callido improbo quaerimus, qualis Q. Nam quibus rebus efficiuntur voluptates, eae non sunt in potestate sapientis. Negare non possum. Huic mori optimum esse propter desperationem sapientiae, illi propter spem vivere... Si probarem, quae ille diceret? Qua-vere falsone, quaerere mittimus-dictum oculis se privavisse.</p>
</section>

<section class="team">
  <h2 class="section-title"><span class="title-dot"></span>Our Team</h2>
  <svg class="arrow" style="left:178px;top:212px" viewBox="0 0 24 40"><path d="M18 6L6 20l12 14" stroke="#22a03c" stroke-width="5" fill="none"/></svg>
  <div class="members">
    <article class="member"><div class="avatar" role="img" aria-label="Portrait of team member"></div><h4>Marlow</h4><p class="role">Lorem ipsum dolor sit amet, consectetur</p><div class="contact"><span><i></i>+1 555 010 2233</span><span><i></i>team@brookforge.example</span></div></article>
    <article class="member"><div class="avatar" role="img" aria-label="Portrait of team member"></div><h4>Ignacio</h4><p class="role">Lorem ipsum dolor sit amet, consectetur</p><div class="contact"><span><i></i>+1 555 010 2233</span><span><i></i>team@brookforge.example</span></div></article>
    <article class="member"><div class="avatar" role="img" aria-label="Portrait of team member"></div><h4>Fletcher</h4><p class="role">Lorem ipsum dolor sit amet, consectetur</p><div class="contact"><span><i></i>+1 555 010 2233</span><span><i></i>team@brookforge.example</span></div></article>
    <article class="member"><div class="avatar" role="img" aria-label="Portrait of team member"></div><h4>Bartholomew</h4><p class="role">Lorem ipsum dolor sit amet, consectetur</p><div class="contact"><span><i></i>+1 555 010 2233</span><span><i></i>team@brookforge.example</span></div></article>
  </div>
  <svg class="arrow" style="left:998px;top:212px" viewBox="0 0 24 40"><path d="M6 6l12 14L6 34" stroke="#22a03c" stroke-width="5" fill="none"/></svg>
</section>

<section class="signup">
  <h3>Sign up now, stay touch &amp; start earning</h3>
  <div class="field"><i></i>Your Name</div>
  <div class="field"><i></i>Your E-Mail</div>
  <div class="submit">Submit</div>
</section>

<section class="testimonials">
  <h2 class="section-title"><span class="title-dot"></span>Testimonials</h2>
  <div class="quotes">
    <div class="quote"><div class="avatar" role="img" aria-label="Customer portrait"></div><div><p>Lorem ipsum dolor sit amet, per saltus semper et conubia latine dissentiunt ut, ea vis graeci consequat inveniam. Tantas facilisi quaerendum in has.</p><div class="who"><b>Orwin</b> a happy customer</div></div></div>
    <div class="quote"><div class="avatar" role="img" aria-label="Customer portrait"></div><div><p>Lorem ipsum dolor sit amet, per saltus semper et conubia latine dissentiunt ut, ea vis graeci consequat inveniam. Tantas facilisi quaerendum in has.</p><div class="who"><b>Calder</b> a happy customer</div></div></div>
    <div class="quote"><div class="avatar" role="img" aria-label="Customer portrait"></div><div><p>Lorem ipsum dolor sit amet, per saltus semper et conubia latine dissentiunt ut, ea vis graeci consequat inveniam. Tantas facilisi quaerendum in has.</p><div class="who"><b>Linnea</b> a happy customer</div></div></div>
    <div class="quote"><div class="avatar" role="img" aria-label="Customer portrait"></div><div><p>Lorem ipsum dolor sit amet, per saltus semper et conubia latine dissentiunt ut, ea vis graeci consequat inveniam. Tantas facilisi quaerendum in has.</p><div class="who"><b>Rowan</b> a happy customer</div></div></div>
  </div>
</section>

<footer>
  <div class="footer">
    <div class="col-brand">
      <div class="brand"><span class="brand-dot"></span>Brook Forge</div>
      <p>Lorem ipsum dolor sit amet, consectetur adipiscing elit. Quid autem habent admirations, cum prope accessit?</p>
      <div class="lines">
        <span>410 Fernwick Road</span>
        <span>Juniper Falls, OR 97001</span>
        <span><i></i>416-555-0187</span>
        <span><i></i>hello@brookforge.example</span>
        <span><i></i>www.brookforge.example</span>
      </div>
    </div>
    <div class="col-links">
      <h5>Quick Link</h5>
      <ul><li>Home</li><li>About</li><li>Services</li><li>Cloud Mining</li><li>Why Us</li><li>Our Team</li><li>Contact Us</li></ul>
    </div>
    <div class="col-follow">
      <h5>Follow Us On</h5>
      <div class="social"><span></span><span></span><span></span><span></span></div>
      <div class="call"><h5>Call Us On</h5><strong>416-555-0187</strong></div>
    </div>
  </div>
  <div class="bottombar">© 2017 Brook Forge | Privacy Policy | User Agreement</div>
</footer>

</body>
</html>
```